Graduation Yearbook Page for a Young Lady

A one page for my daughter's yearbook. She is in 8th grade, which in her school is the year they graduate and go to different highschools. I am looking for a clean and elegant and yet imaginative layout that incorporates "Tessa, Congratulations, We are so very proud of you. Mom, Dad, Grandma, Joan and Harold.
Please feel free as many or as few as 4 of the attached photos. The main photo Tessa Smiling should be in the center.

```html
<!DOCTYPE html>
<html lang="en">
<head>
<meta charset="utf-8">
<title>Tessa – Graduation Page</title>
<link rel="stylesheet" href="https://fonts.googleapis.com/css2?family=Pinyon+Script&display=swap">
<style>
  :root {
    --page: #ffffff;
    --gold: #a8860e;
    --gold-deep: #94740a;
    --portrait-dark: #0c0908;
    --portrait-hair: #b86a34;
    --portrait-skin: #e3a789;
    --sky: #4a82d0;
    --sky-light: #7fa9e3;
    --dress-pink: #e86a8e;
    --room-dark: #1e140e;
    --room-brown: #3a2a1e;
    --child-skin: #d9a88c;
    --hair-light: #a88458;
    --cap-red: #b8262c;
  }
  * { margin: 0; padding: 0; box-sizing: border-box; }
  html, body {
    width: 1200px;
    height: 926px;
    overflow: hidden;
    background: var(--page);
  }
  .page {
    position: relative;
    width: 1200px;
    height: 926px;
    background: var(--page);
  }
  .photo-cluster {
    position: absolute;
    inset: 0;
    width: 1200px;
    height: 926px;
  }
  .message {
    position: absolute;
    left: 0;
    top: 0;
    width: 1200px;
    height: 926px;
    font-family: "Pinyon Script", cursive;
    color: var(--gold);
    line-height: 1;
    pointer-events: none;
  }
  .message span {
    position: absolute;
    left: 68px;
    white-space: nowrap;
  }
  .message__name {
    top: 550px;
    font-size: 52px;
    color: var(--gold-deep);
  }
  .message__headline {
    top: 634px;
    font-size: 95px;
  }
  .message__line {
    top: 743px;
    font-size: 56px;
  }
  .message__signoff {
    top: 828px;
    font-size: 56px;
  }
</style>
</head>
<body>
<main class="page">
  <svg class="photo-cluster" viewBox="0 0 1200 926" xmlns="http://www.w3.org/2000/svg">
    <defs>
      <linearGradient id="outing-tones" x1="0" y1="0" x2="0" y2="1">
        <stop offset="0" stop-color="var(--sky)"/>
        <stop offset="0.55" stop-color="var(--sky-light)"/>
        <stop offset="0.8" stop-color="var(--dress-pink)"/>
        <stop offset="1" stop-color="#e9e6e2"/>
      </linearGradient>
      <radialGradient id="portrait-tones" cx="0.48" cy="0.55" r="0.6">
        <stop offset="0" stop-color="var(--portrait-skin)"/>
        <stop offset="0.45" stop-color="var(--portrait-hair)"/>
        <stop offset="1" stop-color="var(--portrait-dark)"/>
      </radialGradient>
      <linearGradient id="crown-tones" x1="0" y1="0" x2="0" y2="1">
        <stop offset="0" stop-color="var(--cap-red)"/>
        <stop offset="0.35" stop-color="var(--hair-light)"/>
        <stop offset="0.7" stop-color="var(--child-skin)"/>
        <stop offset="1" stop-color="var(--room-dark)"/>
      </linearGradient>
      <radialGradient id="dance-tones" cx="0.5" cy="0.55" r="0.6">
        <stop offset="0" stop-color="var(--child-skin)"/>
        <stop offset="0.5" stop-color="var(--hair-light)"/>
        <stop offset="1" stop-color="var(--room-brown)"/>
      </radialGradient>
    </defs>

    <g class="photo photo--outing" role="img" aria-label="Photo of Tessa as a young girl in sunglasses and a headscarf by a river railing, a bridge and blue sky behind">
      <circle cx="738" cy="377" r="222" fill="url(#outing-tones)"/>
    </g>

    <g class="photo photo--portrait" role="img" aria-label="Portrait of Tessa smiling, long auburn hair, on a black background">
      <circle cx="300" cy="290" r="263" fill="url(#portrait-tones)" stroke="var(--page)" stroke-width="6"/>
    </g>

    <g class="photo photo--crown" role="img" aria-label="Photo of Tessa as a toddler wearing a red paper crown">
      <circle cx="998" cy="243" r="150" fill="url(#crown-tones)" stroke="var(--page)" stroke-width="6"/>
    </g>

    <g class="photo photo--dance" role="img" aria-label="Photo of Tessa as a small girl with a bob haircut in a white top">
      <circle cx="1018" cy="624" r="162" fill="url(#dance-tones)" stroke="var(--page)" stroke-width="6"/>
    </g>
  </svg>

  <p class="message">
    <span class="message__name">Tessa,</span>
    <span class="message__headline">Congratulations,</span>
    <span class="message__line">We are so very proud of you.</span>
    <span class="message__signoff">Mom, Dad, Grandma, Joan and Harold.</span>
  </p>
</main>
</body>
</html>
```